Reed & Vale NC grand opening (for BILLBOARD)

Advertising the grand opening of our cannabis/hemp shop in NC. We will sell all things hemp (flower, cartridges, disposables, edibles, creams, lotions, pet products etc...)

Requirements
Must have
• include, open starting Aug 1, but grand opening Aug 15th.
Nice to have
• Difference slogan ideas "Save some cash, buy our grass" "Find your perfect high at Reed & Vale cannabis store" "Experience Nature's Gift: Reed & Vale Cannabis Store"

```html
<!DOCTYPE html>
<html lang="en">
<head>
<meta charset="utf-8">
<title>Reed &amp; Vale Grand Opening Billboard</title>
<link href="https://fonts.googleapis.com/css2?family=Poppins:wght@400;500;700;800&family=Dancing+Script:wght@600&display=swap" rel="stylesheet">
<style>
  :root {
    --backdrop: #b3b3b3;
    --leaf-green: #6cc04a;
    --deep-green: #1f6e3a;
    --ink-navy: #151b36;
    --mist: #f6faf1;
    --wash: #d6ebc2;
    --white: #ffffff;
  }
  * { margin: 0; padding: 0; box-sizing: border-box; }
  html, body {
    width: 1200px; height: 442px; overflow: hidden;
    background: var(--backdrop);
  }
  .billboard {
    position: absolute; left: 56px; top: 60px;
    width: 1087px; height: 320px;
    background: var(--mist);
    overflow: hidden;
    font-family: "Poppins", sans-serif;
    color: var(--ink-navy);
  }
  .billboard__wash {
    position: absolute; inset: 0;
    background:
      radial-gradient(ellipse 38% 55% at 50% 50%, rgba(255,255,255,0.95), rgba(255,255,255,0) 100%),
      linear-gradient(90deg, var(--wash) 0%, rgba(230,242,218,0.6) 22%, rgba(246,250,241,0.2) 45%, rgba(246,250,241,0.2) 60%, rgba(230,242,218,0.6) 80%, var(--wash) 100%);
  }
  .floral { position: absolute; top: 0; bottom: 0; width: 240px; }
  .floral--left { left: 0; background: linear-gradient(90deg, rgba(160,210,120,0.25), rgba(160,210,120,0)); }
  .floral--right { right: 0; background: linear-gradient(270deg, rgba(160,210,120,0.25), rgba(160,210,120,0)); }

  .brand {
    position: absolute; left: 0; right: 0; top: 62px;
    padding-left: 33px;
    text-align: center;
    font-weight: 500; font-size: 54px; line-height: 1;
    color: var(--leaf-green);
    letter-spacing: -1px;
    white-space: nowrap;
  }

  .tagline__line {
    position: absolute; right: 549px;
    font-size: 29px; line-height: 1; font-weight: 400;
    white-space: nowrap; text-align: right;
  }
  .tagline__line--one { top: 135px; }
  .tagline__line--two { top: 171px; }
  .tagline__line--three { top: 212px; }
  .tagline__line strong { color: var(--leaf-green); font-weight: 700; }
  .tagline__date { font-weight: 700; color: var(--leaf-green); }
  .tagline__date sup { font-size: 17px; line-height: 0; vertical-align: 11px; }

  .divider {
    position: absolute; left: 563px; top: 138px;
    width: 2px; height: 109px; background: var(--ink-navy);
  }

  .headline-grand {
    position: absolute; left: 592px; top: 129px;
    font-weight: 700; font-size: 64px; line-height: 1;
    color: var(--leaf-green); letter-spacing: -1px;
    white-space: nowrap;
  }
  .headline-opening {
    position: absolute; left: 585px; top: 172px;
    font-family: "Dancing Script", cursive; font-weight: 600;
    font-size: 76px; line-height: 1;
    color: var(--deep-green);
    white-space: nowrap;
  }
  .date-day {
    position: absolute; left: 807px; top: 140px;
    font-weight: 800; font-size: 58px; line-height: 1;
    letter-spacing: -1px; white-space: nowrap;
  }
  .date-day sup { font-size: 28px; line-height: 0; vertical-align: 22px; letter-spacing: 0; }
  .date-month {
    position: absolute; left: 807px; top: 187px;
    font-weight: 800; font-size: 60px; line-height: 1;
    white-space: nowrap;
  }

  .location {
    position: absolute; left: 452px; top: 268px;
    width: 184px; height: 24px; border-radius: 12px;
    background: var(--ink-navy); color: var(--white);
    font-size: 12.5px; font-weight: 500;
    display: flex; align-items: center; justify-content: center;
    white-space: nowrap;
  }
</style>
</head>
<body>
  <section class="billboard">
    <div class="billboard__wash"></div>
    <div class="floral floral--left" role="img" aria-label="Soft green line-art of poppies and leaves"></div>
    <div class="floral floral--right" role="img" aria-label="Soft green line-art of poppies and leaves"></div>

    <div class="brand">Reed &amp; Vale</div>

    <p class="tagline">
      <span class="tagline__line tagline__line--one">Find your perfect high at</span>
      <span class="tagline__line tagline__line--two"><strong>Reed &amp; Vale cannabis</strong> store</span>
      <span class="tagline__line tagline__line--three">Open starting <span class="tagline__date">1<sup>st</sup> Aug</span></span>
    </p>

    <div class="divider"></div>

    <div class="headline-grand">Grand</div>
    <div class="headline-opening">Opening</div>
    <div class="date-day">15<sup>TH</sup></div>
    <div class="date-month">AUG</div>

    <div class="location">Exit 4B Maple Ridge Rd</div>
  </section>
</body>
</html>
```